Business Card Design Project

I need a business card design for an Organic drive thru coffee kiosk. We will serve organic coffee, teas & smoothies and will serve healthy breakfast food/snacks for people on the go.
I want the card to have 2-3 colors max (earthy colors like browns, greens and so on).
I have attached the logo I want used and would love to play off the theme of "balance."
Include:
Tidy-Kettle Coffee
address: 4820 Gorvin Ct. Raleigh, NC 27583
phone: 919-731-4062
website: www.tidy-kettle.com (website is not up yet but still include it on card)
email: Rosalind@tidy-kettle.com
I want one of the following sayings somewhere on the card (the front or back is fine):
"Break the fast with Tidy-Kettle"
"Break the fast with Tidy-Kettle"
Maybe on the back list what we offer:
-Organic coffee, espresso & tea
-Blendora smoothies & protein shakes
-Zesty Pour (100% fresh local fruit and veggies)
-Tender Nibs

```html
<!DOCTYPE html>
<html lang="en">
<head>
<meta charset="utf-8">
<title>Tidy-Kettle Coffee — Business Card</title>
<link rel="stylesheet" href="https://fonts.googleapis.com/css2?family=Open+Sans:wght@400;600&display=swap">
<style>
  :root {
    --backdrop: #111111;
    --front-light: #5b3620;
    --front-dark: #3a2213;
    --back-light: #2e1c11;
    --back-dark: #1b100a;
    --ink-light: #ffffff;
    --ink-soft: #e9e2dc;
    --ink-muted: #8c8781;
    --mark: #dcdcdc;
  }
  * { margin: 0; padding: 0; box-sizing: border-box; }
  html, body {
    width: 903px;
    height: 1200px;
    overflow: hidden;
    background: var(--backdrop);
    font-family: "Open Sans", sans-serif;
  }
  .canvas {
    position: relative;
    width: 903px;
    height: 1200px;
  }
  .card {
    position: absolute;
    left: 130px;
    width: 645px;
    height: 368px;
    box-shadow: 0 8px 24px rgba(0, 0, 0, 0.6);
    text-align: center;
  }
  .card--front {
    top: 121px;
    background: radial-gradient(ellipse 90% 80% at 50% 0%, var(--front-light), var(--front-dark));
  }
  .card--back {
    top: 656px;
    background: radial-gradient(ellipse 90% 80% at 50% 10%, var(--back-light), var(--back-dark));
  }
  .brand {
    position: absolute;
    top: 34px;
    left: 0;
    right: 0;
  }
  .brand__dot {
    display: block;
    width: 70px;
    height: 70px;
    margin: 0 auto;
    border-radius: 50%;
    background: var(--mark);
  }
  .brand__name {
    margin-top: 12px;
    font-size: 50px;
    font-weight: 600;
    line-height: 1.1;
    color: var(--ink-light);
    letter-spacing: -0.5px;
  }
  .brand__tagline {
    margin-top: 6px;
    font-size: 12px;
    font-weight: 600;
    letter-spacing: 2.6px;
    color: var(--ink-soft);
  }
  .contact {
    position: absolute;
    top: 233px;
    left: 0;
    right: 0;
    list-style: none;
    font-size: 15px;
    line-height: 20px;
    color: var(--ink-light);
  }
  .slogan {
    position: absolute;
    top: 161px;
    left: 0;
    right: 0;
    font-size: 30px;
    font-weight: 400;
    color: var(--ink-muted);
  }
</style>
</head>
<body>
<main class="canvas">
  <section class="card card--front" aria-label="Card front">
    <div class="brand">
      <span class="brand__dot"></span>
      <h1 class="brand__name">Tidy-Kettle</h1>
      <p class="brand__tagline">ORGANIC COFFEE + CAFE</p>
    </div>
    <ul class="contact">
      <li>Tidy-Kettle Coffee</li>
      <li>Address: 4820 Gorvin Ct. Raleigh, NC 27583</li>
      <li>Phone: 919-731-4062</li>
      <li>Website: www.tidy-kettle.com</li>
      <li>Email: Rosalind@tidy-kettle.com</li>
    </ul>
  </section>

  <section class="card card--back" aria-label="Card back">
    <p class="slogan">Break the fast with Tidy-Kettle</p>
  </section>
</main>
</body>
</html>
```